Corvale Pizzeria Vehicle Wrap Design

Looking for a vehicle wrap design for a delivery car that will be used by my business, "Corvale Pizzeria", located in midcoast Maine. We are a traditional house of pizza style restaurant. The vehicle will be either white or red. Looking for designs that will complement those car colors. I am attaching our primary logo that should be incorporated into the main features of the design. Logo colors can be adjusted to fit design themes but would like to see at least one design using the existing gold and blue colors. Interested in modern styling that is sleek and professional. Designs could also include areas for phone number, website, and "Delivery" callout. Design should be for a midsize 4 door sedan or hatchback.

Target Market(s)

25-45 in age, families

Industry/Entity Type

Restaurant/Pizza/Quick Service Food

Font styles to use
Serif
Other font styles liked:
• Copperplate Bold

Colors
0054AA
0677BA
7BADD7
CADEEF
E8F1F8
FFC000
F8CF3A
FAE287
FDF2CF
FEFAEE
EE7325
F08F49
F5BC92
FAE3D3
FDF4ED

Requirements
Must have
• consistent themes built upon existing logo provided with
Nice to have
• designs that will complement blue, gold, white
Should not have
• graphics that are too bold or flashy

```html
<!DOCTYPE html>
<html lang="en">
<head>
<meta charset="utf-8">
<title>Corvale Pizzeria – Delivery Vehicle Wrap</title>
<link rel="stylesheet" href="https://fonts.googleapis.com/css2?family=Cinzel:wght@700;800&family=Roboto:wght@500;700;900&display=swap">
<style>
  :root {
    --navy: #1b2f80;
    --gold: #e6a93b;
    --white: #ffffff;
    --backdrop: #eef1f4;
    --rule: #1b2f80;
  }
  html, body {
    margin: 0;
    padding: 0;
    width: 1200px;
    height: 467px;
    overflow: hidden;
    background: var(--backdrop);
  }
  .wrap-layout {
    display: block;
    width: 1200px;
    height: 467px;
  }
  .panel { fill: var(--white); }
  .band-gold { fill: var(--gold); }
  .field-navy { fill: var(--navy); }
  .rule { stroke: var(--rule); stroke-width: 3; fill: none; }
  .phone-number {
    font-family: "Roboto", Arial, sans-serif;
    font-weight: 700;
    font-size: 25px;
    fill: var(--navy);
  }
  .phone-icon { fill: none; stroke: var(--gold); stroke-width: 2.4; stroke-linecap: round; stroke-linejoin: round; }
  .brand-disc { fill: var(--white); }
  .brand-name {
    font-family: "Cinzel", Georgia, serif;
    font-weight: 800;
    font-size: 19px;
    fill: var(--navy);
    letter-spacing: 1px;
  }
  .band-title {
    font-family: "Cinzel", Georgia, serif;
    font-weight: 800;
    font-size: 46px;
    letter-spacing: 4px;
    fill: var(--navy);
  }
  .web-address {
    font-family: "Cinzel", Georgia, serif;
    font-weight: 700;
    font-size: 14px;
    letter-spacing: 2px;
    fill: var(--navy);
  }
  .delivery-small {
    font-family: "Roboto", Arial, sans-serif;
    font-weight: 500;
    font-size: 12px;
    fill: var(--white);
  }
  .delivery-large {
    font-family: "Roboto", Arial, sans-serif;
    font-weight: 900;
    font-size: 18px;
    fill: var(--gold);
  }
  .courier-mark { fill: var(--gold); }
</style>
</head>
<body>
<svg class="wrap-layout" viewBox="0 0 1200 467" xmlns="http://www.w3.org/2000/svg">
  <defs>
    <clipPath id="panel-clip">
      <rect x="30" y="40" width="1140" height="330" rx="28"/>
    </clipPath>
  </defs>

  <rect class="panel" x="30" y="40" width="1140" height="330" rx="28"/>

  <g clip-path="url(#panel-clip)">
    <!-- upper-right navy corner -->
    <polygon class="field-navy" points="905,40 1000,40 1115,128 1170,130 1170,120 870,193"/>
    <!-- gold diagonal band -->
    <polygon class="band-gold" points="355,303 1170,130 1170,208 430,365 355,370"/>
    <!-- lower navy field with leaf texture area -->
    <polygon class="field-navy" points="430,365 1170,208 1170,370 430,370"
             role="img" aria-label="Navy field with faint olive leaf pattern"/>
  </g>

  <!-- thin rules -->
  <line class="rule" x1="535" y1="264" x2="600" y2="250"/>
  <line class="rule" x1="826" y1="201" x2="870" y2="192"/>
  <line class="rule" x1="350" y1="305" x2="385" y2="298"/>

  <!-- phone -->
  <g class="contact-phone">
    <path class="phone-icon" d="M188,208 c-4,4 -2,12 5,18 c6,6 13,8 17,4 l-4,-5 l-4,2 c-3,-2 -6,-5 -8,-8 l2,-4 z"/>
    <text class="phone-number" x="206" y="225">207-555-0187</text>
  </g>

  <!-- brand mark: plain disc with name -->
  <g class="brand-lockup">
    <circle class="brand-disc" cx="460" cy="285" r="68"/>
    <text class="brand-name" x="460" y="282" text-anchor="middle">Corvale</text>
    <text class="brand-name" x="460" y="305" text-anchor="middle">Pizzeria</text>
  </g>

  <!-- web address -->
  <text class="web-address" transform="translate(600,248) rotate(-12.06)">THECORVALEPIZZA.COM</text>

  <!-- band title -->
  <text class="band-title" transform="translate(555,312) rotate(-12.06)">CORVALE PIZZERIA</text>

  <!-- delivery callout -->
  <g class="delivery-callout">
    <rect class="courier-mark" x="921" y="93" width="36" height="32" rx="6"
          role="img" aria-label="Delivery courier on scooter illustration"/>
    <text class="delivery-small" x="968" y="114">CALL</text>
    <text class="delivery-small" x="971" y="125">FOR</text>
    <text class="delivery-large" x="918" y="143">DELIVERY</text>
  </g>
</svg>
</body>
</html>
```